Sleep Consulting Business

Hello I need a business card design with similar colors to my logo that was created. I help mom/parents whose little ones are having sleep issues. Are you able to recreate the picture with the girl sleeping onto a business card using a picture that I provide. That would be one side with my logo on top and on the other side would the following:
My name (in bigger letters than the rest. maybe written in script
title
email
website
phone
instagram
I have included color Inspo
Full Name, number, email, website, ig page

```html
<!DOCTYPE html>
<html lang="en">
<head>
<meta charset="utf-8">
<title>Drift Softly – Business Card</title>
<link rel="stylesheet" href="https://fonts.googleapis.com/css2?family=Arimo:wght@400;700&family=Dancing+Script:wght@500&display=swap">
<style>
  :root {
    --stage: #e9e6e4;
    --taupe: #978c87;
    --paper: #fbfbfa;
    --ink: #1e1e1e;
    --grey-text: #7f7571;
    --terracotta: #c0876a;
    --rule: #cfc9c6;
  }
  * { margin: 0; padding: 0; box-sizing: border-box; }
  html, body { width: 1200px; height: 912px; overflow: hidden; }
  body {
    background: var(--stage);
    position: relative;
    font-family: "Arimo", Arial, sans-serif;
  }
  .card {
    position: absolute;
    width: 620px;
    height: 354px;
    box-shadow: 0 10px 28px rgba(0,0,0,.18);
  }
  /* Back */
  .card-back {
    left: 60px; top: 70px;
    background: var(--taupe);
    color: #fff;
  }
  .card-back .brand {
    position: absolute;
    top: 118px; left: 0; right: 0;
    display: flex; align-items: center; justify-content: center; gap: 14px;
  }
  .brand-dot {
    width: 30px; height: 30px; border-radius: 50%;
  }
  .card-back .brand-dot { background: #fff; }
  .brand-name {
    font-size: 40px; font-weight: 400; letter-spacing: 1px;
  }
  .card-back .web {
    position: absolute;
    bottom: 70px; left: 0; right: 0;
    text-align: center;
    font-size: 17px; font-weight: 700; letter-spacing: 3px;
  }
  /* Front */
  .card-front {
    left: 520px; top: 488px;
    background: var(--paper);
  }
  .card-front .brand {
    position: absolute;
    left: 34px; top: 150px; width: 240px;
    display: flex; align-items: center; gap: 10px;
  }
  .card-front .brand-dot { background: var(--terracotta); width: 24px; height: 24px; }
  .card-front .brand-name { color: var(--grey-text); font-size: 32px; }
  .divider {
    position: absolute;
    left: 286px; top: 36px;
    width: 1px; height: 232px;
    background: var(--rule);
  }
  .details {
    position: absolute;
    left: 312px; top: 44px;
    color: var(--ink);
  }
  .person-name {
    font-family: "Dancing Script", cursive;
    font-size: 34px; color: var(--grey-text); line-height: 1;
  }
  .person-title {
    font-size: 15px; color: var(--terracotta); margin-top: 4px;
  }
  .address {
    font-size: 16px; line-height: 1.25; margin-top: 14px;
  }
  .contacts { list-style: none; margin-top: 14px; }
  .contacts li {
    display: flex; align-items: center; gap: 10px;
    font-size: 16px; line-height: 23px;
  }
  .contacts svg { width: 13px; height: 13px; flex: none; }
  .band-line {
    position: absolute; left: 0; right: 0;
    bottom: 44px; height: 3px;
    background: var(--terracotta);
  }
  .band {
    position: absolute; left: 0; right: 0;
    bottom: 0; height: 30px;
    background: #eceae9;
    border-top: 1px solid var(--rule);
  }
</style>
</head>
<body>

<section class="card card-back" aria-label="Card back">
  <div class="brand">
    <span class="brand-dot"></span>
    <span class="brand-name">Drift Softly</span>
  </div>
  <p class="web">www.driftsoftly.com</p>
</section>

<section class="card card-front" aria-label="Card front">
  <div class="brand">
    <span class="brand-dot"></span>
    <span class="brand-name">Drift Softly</span>
  </div>
  <div class="divider"></div>
  <div class="details">
    <p class="person-name">Dana Whitfield</p>
    <p class="person-title">Chief of Staff</p>
    <p class="address">218 Linden Ave, Suite 12<br>Fairview, OR 97024</p>
    <ul class="contacts">
      <li>
        <svg viewBox="0 0 16 16" aria-hidden="true"><path fill="#c0876a" d="M3 1.5l2.6-.5 1.5 3.4-1.6 1.2a8 8 0 0 0 4.4 4.4l1.2-1.6 3.4 1.5-.5 2.6c-.2.6-.8 1-1.5 1C6.5 13.5 2.5 9.5 2 3c0-.7.4-1.3 1-1.5z"/></svg>
        (555) 014-2293
      </li>
      <li>
        <svg viewBox="0 0 16 16" aria-hidden="true"><rect x="1" y="3" width="14" height="10" rx="1" fill="#c0876a"/><path d="M1.5 3.8L8 9l6.5-5.2" stroke="#fff" stroke-width="1.3" fill="none"/></svg>
        dana@driftsoftly.com
      </li>
      <li>
        <svg viewBox="0 0 16 16" aria-hidden="true"><circle cx="8" cy="8" r="7" fill="#c0876a"/><path d="M1 8h14M8 1c-3 3.5-3 10.5 0 14M8 1c3 3.5 3 10.5 0 14" stroke="#fff" stroke-width="1" fill="none"/></svg>
        www.driftsoftly.com
      </li>
      <li>
        <svg viewBox="0 0 16 16" aria-hidden="true"><circle cx="8" cy="8" r="7" fill="#c0876a"/></svg>
        @driftsoftly
      </li>
    </ul>
  </div>
  <div class="band-line"></div>
  <div class="band"></div>
</section>

</body>
</html>
```